Carpet cleaning company wants business card

Need an exciting new fresh design for business cards for my carpet cleaning /pest control business
www.tidewellhomecare.com.au
Can design include a lined section for quoting or information? Thanks !

```html
<!DOCTYPE html>
<html lang="en">
<head>
<meta charset="utf-8">
<title>Tidewell Home Care – Business Card</title>
<link href="https://fonts.googleapis.com/css2?family=Rubik:wght@500;700&family=Roboto:wght@400;500&display=swap" rel="stylesheet">
<style>
  :root {
    --stage: #000000;
    --card-navy: #20425f;
    --card-white: #ffffff;
    --brand-red: #ef4040;
    --brand-blue: #0d55a5;
  }
  * { margin: 0; padding: 0; box-sizing: border-box; }
  html, body { width: 1200px; height: 1200px; overflow: hidden; background: var(--stage); }
  .canvas { position: relative; width: 1200px; height: 1200px; }

  .card {
    position: absolute;
    left: 330px;
    width: 549px;
    height: 329px;
    border-radius: 43px;
  }
  .card-front { top: 253px; background: var(--card-navy); }
  .card-back { top: 601px; background: var(--card-white); }

  .brand-name {
    position: absolute;
    left: 0; right: 0;
    text-align: center;
    font-family: "Rubik", sans-serif;
    font-weight: 700;
    font-size: 34px;
    letter-spacing: -0.5px;
    color: var(--brand-red);
    white-space: nowrap;
  }
  .card-front .brand-name { top: 138px; }
  .card-back .brand-name { top: 62px; }

  .holder {
    position: absolute;
    left: 40px;
    width: 225px;
    top: 190px;
    text-align: center;
    font-family: "Rubik", sans-serif;
    color: var(--brand-blue);
  }
  .holder-name { font-weight: 700; font-size: 27px; line-height: 32px; letter-spacing: -0.3px; }
  .holder-role { font-weight: 500; font-size: 20px; line-height: 26px; }

  .divider {
    position: absolute;
    left: 274px;
    top: 170px;
    width: 2px;
    height: 111px;
    background: var(--brand-red);
  }

  .contacts {
    position: absolute;
    left: 294px;
    top: 170px;
    list-style: none;
    font-family: "Roboto", sans-serif;
    font-size: 15.5px;
    font-weight: 400;
    color: var(--brand-blue);
  }
  .contacts li {
    display: flex;
    align-items: flex-start;
    gap: 6px;
    line-height: 17px;
    margin-bottom: 5.5px;
  }
  .contacts svg { width: 12px; height: 12px; flex: none; margin-top: 2px; fill: none; stroke: var(--brand-blue); stroke-width: 1.6; }
  .contacts svg.solid { fill: var(--brand-blue); stroke: none; }
</style>
</head>
<body>
<div class="canvas">

  <section class="card card-front">
    <div class="brand-name">Tidewell Home Care</div>
  </section>

  <section class="card card-back">
    <div class="brand-name">Tidewell Home Care</div>

    <div class="holder">
      <div class="holder-name">Darren HOLLIS</div>
      <div class="holder-role">Director</div>
    </div>

    <div class="divider"></div>

    <ul class="contacts">
      <li>
        <svg class="solid" viewBox="0 0 24 24"><path d="M6.6 10.8a15 15 0 0 0 6.6 6.6l2.2-2.2a1 1 0 0 1 1-.25 11.4 11.4 0 0 0 3.6.57 1 1 0 0 1 1 1V20a1 1 0 0 1-1 1A17 17 0 0 1 3 4a1 1 0 0 1 1-1h3.5a1 1 0 0 1 1 1c0 1.25.2 2.45.57 3.57a1 1 0 0 1-.25 1z"/></svg>
        <span>123-555-0147</span>
      </li>
      <li>
        <svg viewBox="0 0 24 24"><rect x="2" y="5" width="20" height="14" rx="1"/><path d="M2 6l10 7 10-7M2 19l7-6M22 19l-7-6"/></svg>
        <span>info@tidewellhomecare.au</span>
      </li>
      <li>
        <svg viewBox="0 0 24 24"><circle cx="12" cy="12" r="10"/><ellipse cx="12" cy="12" rx="4.5" ry="10"/><path d="M2 12h20M4 7h16M4 17h16"/></svg>
        <span>www.tidewellhomecare.com.au</span>
      </li>
      <li>
        <svg class="solid" viewBox="0 0 24 24"><path d="M12 2a7 7 0 0 0-7 7c0 5 7 13 7 13s7-8 7-13a7 7 0 0 0-7-7zm0 9.5A2.5 2.5 0 1 1 12 6.5a2.5 2.5 0 0 1 0 5z"/></svg>
        <span>312-314, 15920 84 Ave,<br>Delta, BC, V4N 2K7</span>
      </li>
    </ul>
  </section>

</div>
</body>
</html>
```